Book Cover for Self Help Book Teens

I need a standard a5 size book cover (front and back) for my new self help book for teens. The book is called
WHEN DAYS DRAG
ideas and tactics for teens in tough times
break ups, school problems, procrastination, fights, sexuality, alcohol, bitchiness, eating problems, can’t sleep, no motivation, not allowed to do stuff, being on the outer..and 34 other common situations that every day Australian teens face
Brenna Faldow
psychologist for teens
I would like a very sparse,very modern cover, no photos - maybe just cartoon-y graphic of smiley face upside down - ie frowny face. Few colours in order to make it look bold. lots of space on the cover.
I will provide back cover text soon
Updates
I just want to say that I really appreciate all of your efforts, the designs were excellent. As a thankyou, I'm happy to email you a link to the e-version of this book if you are interested. Just email me at brennafaldow@quillmarsh.example and I will send it through as soon as it is completed.
Target Market(s)
teens....but parents will also be buying book
Industry/Entity Type
School
Look and feel

```html
<!DOCTYPE html>
<html lang="en">
<head>
<meta charset="utf-8">
<title>When Days Drag — Book Cover</title>
<link rel="stylesheet" href="https://fonts.googleapis.com/css2?family=Cabin+Sketch:wght@400;700&family=Ubuntu:wght@400&family=Special+Elite&family=Exo+2:wght@300&display=swap">
<style>
  :root {
    --cover-green: #8fbf3f;
    --deep-green: #2f8a3e;
    --pale-green: #bcdc8c;
    --white: #ffffff;
  }
  html, body {
    margin: 0;
    padding: 0;
    overflow: hidden;
    background: var(--cover-green);
  }
  .cover {
    position: relative;
    width: 845px;
    height: 1200px;
    background: var(--cover-green);
    overflow: hidden;
  }
  .title {
    position: absolute;
    top: 120px;
    left: 0;
    width: 100%;
    margin: 0;
    text-align: center;
    font-family: "Cabin Sketch", cursive;
    font-weight: 700;
    font-size: 112px;
    line-height: 142px;
    letter-spacing: 46px;
    color: var(--white);
  }
  .title span { display: block; padding-left: 46px; }
  .subtitle {
    position: absolute;
    top: 562px;
    left: 0;
    width: 100%;
    margin: 0;
    text-align: center;
    font-family: "Ubuntu", sans-serif;
    font-size: 37px;
    line-height: 58px;
    color: var(--deep-green);
  }
  .figures {
    position: absolute;
    top: 772px;
    left: 314px;
    width: 218px;
    height: 90px;
  }
  .author {
    position: absolute;
    top: 932px;
    left: 0;
    width: 100%;
    margin: 0;
    text-align: center;
    font-family: "Special Elite", monospace;
    font-size: 24px;
    letter-spacing: 7px;
    color: var(--white);
  }
  .author-role {
    position: absolute;
    top: 978px;
    left: 0;
    width: 100%;
    margin: 0;
    text-align: center;
    font-family: "Exo 2", sans-serif;
    font-weight: 300;
    font-size: 23px;
    color: var(--deep-green);
  }
  .topics {
    position: absolute;
    top: 1032px;
    left: 6px;
    width: 833px;
    margin: 0;
    font-family: "Exo 2", sans-serif;
    font-weight: 300;
    font-size: 20.5px;
    line-height: 40px;
    color: var(--pale-green);
    letter-spacing: 0.2px;
  }
  .topics span.line {
    display: block;
    text-align: justify;
    text-align-last: justify;
    white-space: nowrap;
    overflow: hidden;
  }
  .topics span.line.last { text-align-last: left; }
  .topics em {
    font-style: normal;
    color: var(--deep-green);
  }
</style>
</head>
<body>
  <main class="cover">
    <h1 class="title"><span>WHEN</span><span>DAYS</span><span>DRAG</span></h1>
    <p class="subtitle">ideas and tactics for<br>teens in tough times</p>
    <svg class="figures" viewBox="0 0 218 90" role="img" aria-label="Three small cartoon teen figures with unhappy expressions">
      <rect x="0" y="0" width="218" height="90" rx="10" fill="#2f8a3e"/>
    </svg>
    <p class="author">BRENNA FALDOW</p>
    <p class="author-role">psychologist for teens</p>
    <p class="topics">
      <span class="line">break ups, <em>school problems</em>, procrastination, fights, <em>sexuality</em>, alcohol, bitchiness,</span>
      <span class="line">eating problems, <em>can’t sleep</em>, no motivation, not allowed to do stuff, being on the</span>
      <span class="line last">outer.. and <em>34 other</em> common <em>situations</em> that every day <em>Australian teens</em> face</span>
    </p>
  </main>
</body>
</html>
```